Redesign Of Current Landing Page

I need to redesign this landing page https://www.brightoakpromos.biz/?page=landing&landing=23 (Please do not opt in because when you do it will show you the home page. Please clear your cookies before going to this url above to view the 1 page landing page.)

Please use my updated website as a reference for colors and logo.
http://layoutcraftzone.com/dh/bopg/index.html

I would like the call to action to be a button that opens into a lead form...

Button would be "Download Samples"

small business owners

Marketing

1 page

Designer to choose colors to be used in the design.

• must be full responsive on all devices
• must have a legitimate professional apeal to it
• open

```html
<!DOCTYPE html>
<html lang="en">
<head>
<meta charset="utf-8">
<title>Bright Oak Promotions Group – Attract More Customers</title>
<link href="https://fonts.googleapis.com/css2?family=Open+Sans:ital,wght@0,400;0,600;0,700;0,800;1,400&display=swap" rel="stylesheet">
<style>
:root{
  --blue:#1b78cc;
  --blue-dark:#0f5aa3;
  --navy:#0b3f73;
  --yellow:#f6c21b;
  --ink:#2b2b2b;
  --muted:#555;
  --white:#fff;
}
*{box-sizing:border-box;margin:0;padding:0}
html,body{width:678px;height:1200px;overflow:hidden;background:var(--white)}
body{font-family:"Open Sans",Arial,sans-serif;color:var(--ink);position:relative}
.site-header{height:68px;display:flex;align-items:center;justify-content:center;gap:8px}
.brand-mark{width:16px;height:16px;border-radius:50%;background:var(--blue)}
.brand-name{font-weight:800;font-size:22px;color:var(--navy);letter-spacing:1px}

.hero{position:relative;height:395px}
.hero-photo{position:absolute;inset:0;background:linear-gradient(160deg,#2f8fd0 0%,#55b6d8 45%,#1e6fb0 100%)}
.hero-title{position:absolute;top:18px;width:100%;text-align:center;color:var(--white);font-weight:800;font-size:30px;letter-spacing:1px}
.hero-sub{position:absolute;top:58px;width:100%;text-align:center;color:var(--white);font-size:12px}
.hero-tagline{position:absolute;left:60px;top:240px;color:var(--white);font-weight:800;font-size:34px}
.hero-copy{position:absolute;left:430px;top:150px;width:248px;height:245px;background:var(--white);padding:16px 14px 0 20px;font-size:10.5px;line-height:1.55;color:var(--muted);text-align:center}

.lead-form{position:absolute;left:255px;top:80px;width:160px;background:var(--yellow);padding:6px 10px 12px;box-shadow:0 3px 10px rgba(0,0,0,.2)}
.lead-form .form-toggle{display:block;margin:0 auto 10px;background:#f9d44d;border:1px solid #e0a800;color:var(--white);font-size:9px;font-weight:700;padding:3px 14px;text-align:center}
.lead-form h3{color:var(--white);font-size:14px;font-weight:700;margin-bottom:6px}
.lead-form label{display:block;color:var(--white);font-size:9.5px;font-weight:700;margin-top:3px}
.lead-form .field{height:14px;background:var(--white);width:100%}
.lead-form .send{display:block;margin:10px auto 0;width:62px;height:16px;background:var(--white);font-size:9px;color:var(--ink);text-align:center;line-height:16px}

.how{background:var(--blue);height:192px;text-align:center;color:var(--white);padding-top:20px}
.section-title{font-weight:800;font-size:22px;letter-spacing:.5px}
.how p{font-size:8.6px;line-height:1.5;width:560px;margin:8px auto 0}
.btn-outline{display:inline-block;margin-top:14px;border:1px solid var(--white);color:var(--white);font-size:11px;padding:5px 20px}

.why{height:290px;padding-top:12px;text-align:center}
.why .section-title{color:var(--ink)}
.benefits{display:grid;grid-template-columns:repeat(3,170px);justify-content:center;row-gap:16px;margin-top:18px}
.benefit{display:flex;flex-direction:column;align-items:center}
.benefit-icon{width:62px;height:62px;background:var(--blue);display:flex;align-items:center;justify-content:center}
.benefit-label{margin-top:8px;font-size:11px;font-weight:700;color:var(--navy);line-height:1.35}

.testimonial{position:absolute;top:945px;left:0;width:678px;height:220px;background:var(--blue);display:flex}
.testimonial-photo{width:305px;height:220px;background:linear-gradient(135deg,#c9a58a,#8a6a55 60%,#4b5f7a)}
.testimonial-body{position:relative;flex:1;padding:18px 48px 0;color:var(--white);text-align:center;font-size:10px;line-height:1.5}
.quote-mark{position:absolute;font-size:64px;font-weight:800;line-height:1;color:var(--white)}
.quote-open{left:10px;top:0}
.quote-close{right:12px;bottom:6px}
.testimonial-author{margin-top:8px;font-size:11px}

.site-footer{position:absolute;top:1165px;left:0;width:678px;height:35px;background:var(--navy);color:var(--white);font-size:9px;display:flex;align-items:center;justify-content:center}
</style>
</head>
<body>
<header class="site-header">
  <span class="brand-mark"></span><span class="brand-name">BOPG</span>
</header>

<section class="hero">
  <div class="hero-photo" role="img" aria-label="Group of happy people jumping against a blue sky"></div>
  <h1 class="hero-title">ATTRACT MORE CUSTOMERS</h1>
  <p class="hero-sub">who spend more money with your business more often</p>
  <p class="hero-tagline">IMAGINE...</p>

  <form class="lead-form">
    <span class="form-toggle">DOWNLOAD SAMPLES</span>
    <h3>Enter Your Info</h3>
    <label>Name</label><div class="field"></div>
    <label>Phone</label><div class="field"></div>
    <label>Email</label><div class="field"></div>
    <div class="send">Send</div>
  </form>

  <div class="hero-copy">
    being able to create exciting give away offers that will boost your sales without ever having to worry about cost. Bright Oak Promotions Group, Inc. provides high perceived value promotional products to businesses that want to advertise a give away that will instantly attract new customers from your existing advertising offers. Your business can give away incentive certificates that are redeemable for luxury hotel &amp; resort stays with airfare included, cruises, getaways, dining and even electronic goods.
  </div>
</section>

<section class="how">
  <h2 class="section-title">HOW CAN WE DO IT?</h2>
  <p>We help fill empty rooms for thousands of hotels and resorts in hundreds of destinations around the world as well as the major cruise lines. Hotels and resorts are rarely full so when we place someone in their empty rooms, they end up making it up when travelers spend money on room service, spa services, eat at their in-house restaurants, casinos and take advantage of other amenities that drive revenue. We also help over 18,000 restaurants, attraction manufacturers, the major gas companies and top grocery chains in the U.S and Canada increase brand awareness as well as increase customer loyalty.</p>
  <span class="btn-outline">DOWNLOAD SAMPLES</span>
</section>

<section class="why">
  <h2 class="section-title">WHY OFFER INCENTIVES TO CUSTOMERS?</h2>
  <div class="benefits">
    <div class="benefit">
      <div class="benefit-icon"><svg width="34" height="34" viewBox="0 0 34 34" fill="none" stroke="#fff" stroke-width="2"><path d="M5 13h6l12-7v22l-12-7H5z"/><path d="M9 21l2 8h4l-2-8"/></svg></div>
      <div class="benefit-label">Increase Responses From<br>Your Existing Ads</div>
    </div>
    <div class="benefit">
      <div class="benefit-icon"><svg width="34" height="34" viewBox="0 0 34 34" fill="none" stroke="#fff" stroke-width="2"><rect x="5" y="13" width="24" height="16"/><rect x="3" y="9" width="28" height="5"/><path d="M17 9v20M17 9c-3-6-9-4-6 0M17 9c3-6 9-4 6 0"/></svg></div>
      <div class="benefit-label">#1 Sales Closing Tool<br>- Gift w/ Purchase</div>
    </div>
    <div class="benefit">
      <div class="benefit-icon"><svg width="34" height="34" viewBox="0 0 34 34" fill="none" stroke="#fff" stroke-width="2"><path d="M3 15l7-5 7 4 7-4 7 5"/><path d="M10 18l6 6c1 1 3 1 3-1l4 2c2 0 3-2 2-3l-6-6"/><path d="M3 15l7 8M31 15l-6 7"/></svg></div>
      <div class="benefit-label">Build Brand Awareness<br>and Trust</div>
    </div>
    <div class="benefit">
      <div class="benefit-icon"><svg width="34" height="34" viewBox="0 0 34 34" fill="none" stroke="#fff" stroke-width="2"><circle cx="17" cy="17" r="13"/><path d="M11 17l4 4 8-9"/></svg></div>
      <div class="benefit-label">Ensure The Sale Over<br>Your Competition</div>
    </div>
    <div class="benefit">
      <div class="benefit-icon"><svg width="34" height="34" viewBox="0 0 34 34" fill="none" stroke="#fff" stroke-width="2"><circle cx="11" cy="11" r="4"/><circle cx="23" cy="11" r="4"/><path d="M3 27c0-6 4-9 8-9s8 3 8 9M15 27c0-6 4-9 8-9s8 3 8 9"/></svg></div>
      <div class="benefit-label">Boost Repeat and<br>Referral Business</div>
    </div>
    <div class="benefit">
      <div class="benefit-icon"><svg width="34" height="34" viewBox="0 0 34 34" fill="none" stroke="#fff" stroke-width="2"><path d="M28 17a11 11 0 1 1-3-7.6"/><path d="M26 3v7h-7"/></svg></div>
      <div class="benefit-label">Improve Retention<br>Rates</div>
    </div>
  </div>
</section>

<section class="testimonial">
  <div class="testimonial-photo" role="img" aria-label="Portrait photo of a smiling customer"></div>
  <div class="testimonial-body">
    <span class="quote-mark quote-open">“</span>
    <p>I began using your incentives two years ago to boost lead generation efforts. I have experienced a 50% increase in lead captures. And, even more importantly, my sales have increased as well. The ability to offer unlimited certificates and not having to pay for each certificate I give away is perhaps the best feature of the program, but having the flexibility to email or print certificates for my customer is also wonderful. I even use your hotel bonuses to accelerate my promotions right on my website!</p>
    <p class="testimonial-author">Dana R.<br>Fairview, TN</p>
    <span class="quote-mark quote-close">”</span>
  </div>
</section>

<footer class="site-footer">© 2005-2017 Bright Oak Promotions Group, Inc. All Rights Reserved</footer>
</body>
</html>
```